Stationary for Keeping Steady

we are in the process of creating a more professional image for our company Keeping Steady Paramedical Services. We have recently had a new logo and general brochure designed using artpitchhub and have been impressed by the quality of submissions.

We need:
- Letterhead (A4)
- Business Cards
- With compliments slips
- Email stationary

Letterhead information:
Address - 47 Wattlebrook Drive, Fernhollow Vic 3091
Phone - 1800 462 817
email - enquiries@keepsteady.com.au
Internet - www.keepsteady.com.au
ABN - 82 463 915 207
ACN - 264 871 035

Files need to be able to be edited in Illustrator CS2

Business Cards / with compliments slips / email stationary:
Double sided.
One side to have Name, Mobile number, company phone 1800462817, email, internet address

Files need to be able to be edited in Illustrator CS2 (except email stationary)

Our website is www.keepsteady.com.au for more information. Do not base designs on the website as it will eventually be revised.

Target Market(s)

Australian based businesses, government departments and schools. We specialise in corporate customers rather than public first aid course

Industry/Entity Type

Internet

Requirements
Must have
• Where applicable file to be editable in illustrator CS2 to allow future alterations.

```html
<!DOCTYPE html>
<html lang="en">
<head>
<meta charset="utf-8">
<title>Keeping Steady Paramedical Services – Letterhead</title>
<link rel="stylesheet" href="https://fonts.googleapis.com/css2?family=Dosis:wght@400;700&display=swap">
<style>
  :root {
    --brand-red: #d3252c;
    --ink-dark: #1e1e1e;
    --ink-grey: #5f5f5f;
    --paper: #ffffff;
  }
  html, body {
    margin: 0;
    padding: 0;
    overflow: hidden;
    background: var(--paper);
  }
  .letterhead {
    position: relative;
    width: 902px;
    height: 1200px;
    background: var(--paper);
    overflow: hidden;
    font-family: "Dosis", sans-serif;
  }
  .brand {
    position: absolute;
    top: 32px;
    left: 40px;
    display: flex;
    align-items: flex-start;
  }
  .brand-mark {
    width: 80px;
    height: 80px;
    background: var(--brand-red);
    margin-top: 6px;
  }
  .brand-text {
    margin-left: 36px;
  }
  .brand-name {
    margin: 0;
    color: var(--brand-red);
    font-weight: 700;
    line-height: 1;
  }
  .brand-name-main {
    display: block;
    font-size: 44px;
  }
  .brand-name-sub {
    display: block;
    font-size: 20px;
    margin-top: 4px;
  }
  .registration {
    margin: 6px 0 0;
    font-size: 16px;
    color: var(--ink-grey);
    letter-spacing: 0.2px;
  }
  .separator {
    display: inline-block;
    width: 7px;
    height: 7px;
    background: var(--brand-red);
    margin: 0 6px;
    vertical-align: middle;
  }
  .footer-band {
    position: absolute;
    left: 0;
    top: 1122px;
    width: 902px;
    height: 8px;
    background: linear-gradient(to right, var(--brand-red) 0%, var(--brand-red) 35%, #3a2a2a 65%, var(--ink-dark) 100%);
  }
  .contact {
    position: absolute;
    left: 0;
    top: 1142px;
    width: 902px;
    text-align: center;
    font-size: 19px;
    line-height: 29px;
    color: var(--ink-grey);
    letter-spacing: 0.4px;
  }
  .contact p {
    margin: 0;
  }
</style>
</head>
<body>
  <div class="letterhead">
    <header class="brand">
      <div class="brand-mark" aria-hidden="true"></div>
      <div class="brand-text">
        <h1 class="brand-name">
          <span class="brand-name-main">Keeping Steady</span>
          <span class="brand-name-sub">Paramedical Services Pty Ltd</span>
        </h1>
        <p class="registration">ABN - 82 463 915 207<span class="separator"></span>ACN - 264 871 035</p>
      </div>
    </header>

    <div class="footer-band"></div>
    <footer class="contact">
      <p>Address - 47 Wattlebrook Drive, Fernhollow Vic 3091<span class="separator"></span>Phone - 1800 462 817</p>
      <p>email - enquiries@keepsteady.com.au<span class="separator"></span>Internet - www.keepsteady.com.au</p>
    </footer>
  </div>
</body>
</html>
```